New business card with our logo

we finalized our logo with the help of pixel harbor - now we need a business card using that logo. we are a metal service center providing raw steel and metal products for fabricating, contractors, artists, etc. we have the wording for the back of the card figured out (attached, no deviations from text please), just need help putting it all together.
would like the look of steel somehow incorporated in the design ... would like the black part of the logo to be steel or silver color (the S & BRANLEY)
Other font styles liked:
- calibri, arial, similar to those, modern looking
Colors
Designer to choose colors to be used in the design.
Requirements
Must have
- Back of card must haves are attached (no deviations from wording please).
- FRONT of card:
- logo
- address
- name
- office tel
- cell
- fax
- website
- address
Nice to have
- incorporate the look of steel or element of steel somehow
- names of the staff on front not in all caps, i.e. Rosvita not ROSVITA
- this industry is more industrial, not coffee or flower shop so design should be aligned with that
- design should be classic and tasteful

```html
<!DOCTYPE html>
<html lang="en">
<head>
<meta charset="utf-8">
<title>Branley Steel – Business Card</title>
<link href="https://fonts.googleapis.com/css2?family=Open+Sans:wght@400;600;700&display=swap" rel="stylesheet">
<style>
  :root {
    --page: #1a1a1a;
    --card: #262525;
    --ink: #ffffff;
    --muted: #d8d8d8;
    --blue: #1f78c8;
    --steel-light: #f2f2f2;
    --steel-mid: #bdbdbd;
    --steel-dark: #8a8a8a;
    --icon-bg: #bcbcbc;
    --icon-ink: #262525;
  }
  * { box-sizing: border-box; margin: 0; padding: 0; }
  html, body { width: 1200px; height: 900px; overflow: hidden; }
  body {
    background: var(--page);
    font-family: "Open Sans", Arial, sans-serif;
    color: var(--ink);
    display: flex;
    flex-direction: column;
    align-items: center;
    justify-content: center;
    gap: 32px;
  }
  .card {
    position: relative;
    width: 620px;
    height: 354px;
    background: var(--card);
    overflow: hidden;
    box-shadow: 0 12px 30px rgba(0,0,0,.5);
  }

  /* front */
  .brand-block {
    position: absolute;
    top: 26px;
    right: 34px;
    text-align: right;
  }
  .brand-lockup {
    display: flex;
    align-items: center;
    justify-content: flex-end;
    gap: 10px;
    font-weight: 700;
    font-size: 24px;
    letter-spacing: .5px;
    color: var(--ink);
  }
  .brand-dot {
    width: 30px; height: 30px;
    border-radius: 50%;
    border: 3px solid var(--blue);
  }
  .service-title {
    margin-top: 14px;
    font-weight: 700;
    font-size: 15px;
    color: var(--blue);
    letter-spacing: .5px;
    padding-bottom: 4px;
    border-bottom: 1px solid var(--muted);
  }
  .service-list {
    margin-top: 4px;
    font-size: 11.5px;
    line-height: 1.5;
    color: var(--muted);
  }
  .contact-list {
    position: absolute;
    list-style: none;
    font-size: 12.5px;
    color: var(--muted);
  }
  .contact-list li {
    display: flex;
    align-items: center;
    gap: 12px;
    margin-bottom: 10px;
    line-height: 1.25;
  }
  .contact-web { top: 218px; left: 330px; }
  .contact-phone { top: 244px; left: 34px; }
  .icon {
    flex: none;
    width: 22px; height: 22px;
    border-radius: 4px;
    background: var(--icon-bg);
    display: flex; align-items: center; justify-content: center;
  }
  .icon svg { width: 14px; height: 14px; fill: var(--icon-ink); }
  .name-band {
    position: absolute;
    top: 126px;
    left: 0;
    width: 300px;
    height: 58px;
    padding: 10px 0 0 30px;
    background: linear-gradient(100deg, var(--steel-light) 0%, var(--steel-mid) 45%, var(--steel-light) 70%, var(--steel-dark) 100%);
  }
  .person-name { font-size: 20px; line-height: 1.1; color: #444; }
  .person-name .first { font-weight: 700; color: var(--blue); }
  .person-role { font-size: 11px; color: #555; }

  /* back */
  .emblem-ring {
    position: absolute;
    right: 38px;
    top: 28px;
    width: 250px; height: 250px;
    border-radius: 50%;
    border: 10px solid var(--steel-mid);
  }
  .back-brand {
    position: absolute;
    left: 40px;
    bottom: 36px;
  }
  .back-name {
    font-weight: 700;
    font-size: 34px;
    letter-spacing: 1px;
    color: var(--steel-mid);
  }
  .back-url { font-size: 13px; color: var(--muted); letter-spacing: .5px; }
</style>
</head>
<body>

  <section class="card card-front">
    <div class="brand-block">
      <div class="brand-lockup"><span class="brand-dot"></span>BRANLEY STEEL</div>
      <div class="service-title">METAL SERVICE CENTER</div>
      <div class="service-list">
        Cut | Shear | Punch | Light Fab<br>
        Structural Steel | Stainless &amp; Aluminum<br>
        Building Components | Rebar | Decking<br>
        and more...
      </div>
    </div>

    <div class="name-band">
      <div class="person-name"><span class="first">Marcus</span> Hale</div>
      <div class="person-role">CEO &amp; Founder</div>
    </div>

    <ul class="contact-list contact-web">
      <li><span class="icon"><svg viewBox="0 0 16 16"><path d="M1 3h14v10H1z M2 4l6 5 6-5" fill="none" stroke="#262525" stroke-width="1.5"/></svg></span>info@branleysteel.com</li>
      <li><span class="icon"><svg viewBox="0 0 16 16"><circle cx="8" cy="8" r="6.5" fill="none" stroke="#262525" stroke-width="1.4"/><path d="M1.5 8h13M8 1.5c3 3 3 10 0 13M8 1.5c-3 3-3 10 0 13" fill="none" stroke="#262525" stroke-width="1.2"/></svg></span>www.branleysteel.com</li>
      <li><span class="icon"><svg viewBox="0 0 16 16"><path d="M8 1a5 5 0 0 0-5 5c0 4 5 9 5 9s5-5 5-9a5 5 0 0 0-5-5zm0 7a2 2 0 1 1 0-4 2 2 0 0 1 0 4z"/></svg></span>1820 Ridge Street<br>Harlow, Illinois 60412</li>
    </ul>

    <ul class="contact-list contact-phone">
      <li><span class="icon"><svg viewBox="0 0 16 16"><path d="M3 1l3 3-2 2c1 2 3 4 5 5l2-2 3 3-2 3C7 14 2 9 1 3z"/></svg></span>555-314-0270</li>
      <li><span class="icon"><svg viewBox="0 0 16 16"><path d="M4 1h8v14H4z M5 2.5v9h6v-9z" fill-rule="evenodd"/></svg></span>555-314-0269</li>
      <li><span class="icon"><svg viewBox="0 0 16 16"><path d="M4 1h6v4H4z M2 6h12v8H2z M4 8v4h3V8z" fill-rule="evenodd"/></svg></span>555-314-0271</li>
    </ul>
  </section>

  <section class="card card-back">
    <div class="emblem-ring"></div>
    <div class="back-brand">
      <div class="back-name">BRANLEY STEEL</div>
      <div class="back-url">www.branleysteel.com</div>
    </div>
  </section>

</body>
</html>
```